Need business card design
Velin Medical
Simple
Tobias Morvel
CEO
12345 any street
city, state 98765
tmorvel@velinmedical.net
www.velinmedical.net
Just looking for design for now. Additional info will be added later

```html
<!DOCTYPE html>
<html lang="en">
<head>
<meta charset="utf-8">
<title>Velin Medical — Stationery</title>
<link rel="stylesheet" href="https://fonts.googleapis.com/css2?family=Nunito:wght@700&family=Open+Sans:wght@400;600&display=swap">
<style>
  :root{
    --backdrop:#a9852c;
    --paper:#ffffff;
    --slate:#3f5566;
    --slate-dark:#34495a;
    --green:#39a64a;
    --grey-flap:#9aa3aa;
    --ink:#4a5560;
    --faint:#e6e9ec;
    --rule:#c9ced3;
  }
  *{box-sizing:border-box;margin:0;padding:0}
  html,body{width:1200px;height:540px;overflow:hidden}
  body{background:var(--backdrop);font-family:"Open Sans",Arial,sans-serif;color:var(--ink);position:relative}
  .piece{position:absolute;background:var(--paper);box-shadow:0 2px 4px rgba(0,0,0,.25);overflow:hidden}
  .brand{display:inline-flex;align-items:center;gap:4px;font-family:"Nunito",Arial,sans-serif;font-weight:700;color:var(--green);white-space:nowrap;line-height:1}
  .brand::before{content:"";width:.8em;height:.8em;background:var(--green);display:block}
  .brand.on-dark{color:#fff}
  .brand.on-dark::before{background:#fff}
  .band{position:absolute;left:0;right:0;bottom:0;height:22px;background:var(--slate);border-top:2px solid var(--green);display:flex;align-items:center;justify-content:space-between;padding:0 18px;font-size:5px;color:#dfe6ea}
  .label{position:absolute;top:496px;font-size:18px;color:#fff}

  .watermark{position:absolute;font-family:"Nunito",Arial,sans-serif;font-weight:700;color:var(--faint);line-height:.95}

  /* letterhead */
  .letterhead{left:30px;top:36px;width:352px;height:442px}
  .letterhead .brand{position:absolute;left:50%;top:14px;transform:translateX(-50%);font-size:11px}
  .letterhead .watermark{left:14px;top:200px;width:220px;font-size:50px}

  /* fax sheet */
  .fax{left:414px;top:36px;width:332px;height:442px}
  .fax .brand{position:absolute;left:46px;top:14px;font-size:11px}
  .fax .contact{position:absolute;right:26px;top:12px;font-size:4.5px;line-height:7px;text-align:left}
  .fax h1{position:absolute;left:28px;top:116px;font-size:16px;font-weight:400;color:var(--ink)}
  .fax .form{position:absolute;left:28px;top:146px;width:276px;display:grid;grid-template-columns:1fr 1fr;column-gap:14px;row-gap:6px;font-size:4.5px}
  .fax .field{border-bottom:1px solid var(--rule);padding-bottom:1px;height:9px}
  .fax .checks{position:absolute;left:28px;top:224px;display:flex;gap:14px;font-size:4.5px}
  .fax .checks span{display:flex;align-items:center;gap:3px}
  .fax .checks span::before{content:"";width:6px;height:6px;border:1px solid var(--ink)}
  .fax .watermark{right:14px;bottom:30px;width:90px;font-size:20px;text-align:right}

  /* envelopes */
  .envelope svg{position:absolute;left:0;top:0}
  .env-back{left:770px;top:70px;width:190px;height:155px}
  .env-back .brand{position:absolute;left:50%;top:22px;transform:translateX(-50%) rotate(180deg);font-size:11px}
  .env-grey{left:880px;top:160px;width:305px;height:148px}
  .env-grey .url{position:absolute;right:14px;bottom:10px;font-size:5px}
  .env-front{left:770px;top:238px;width:290px;height:146px}
  .env-front .flap{position:absolute;left:0;right:0;top:0;height:16px;background:var(--slate)}
  .env-front .brand{position:absolute;left:12px;top:34px;font-size:13px}
  .env-front .address{position:absolute;left:12px;top:52px;font-size:4.5px;line-height:6px}
  .env-front .url{position:absolute;right:12px;bottom:12px;font-size:5px}
  .env-front .stripe{position:absolute;left:0;right:0;bottom:0;height:4px;background:var(--green)}

  /* cards */
  .card-front{left:770px;top:408px;width:142px;height:84px}
  .card-front .top{position:absolute;left:0;right:0;top:0;height:9px;background:var(--slate);font-size:4px;color:#dfe6ea;padding:2px 6px}
  .card-front .brand{position:absolute;left:10px;top:26px;font-size:14px}
  .card-front .lines{position:absolute;left:10px;top:50px;font-size:4px;line-height:5.5px}
  .card-back{left:932px;top:408px;width:138px;height:84px;background:var(--slate)}
  .card-back .brand{position:absolute;left:50%;top:50%;transform:translate(-50%,-50%);font-size:14px}
</style>
</head>
<body>

  <section class="piece letterhead" aria-label="Letterhead">
    <span class="brand">Velin Medical</span>
    <span class="watermark" aria-hidden="true">Velin Medical</span>
    <div class="band">
      <span>T (555) 201-7780</span>
      <span>12345 any street, city, state 98765</span>
      <span>www.velinmedical.net</span>
    </div>
  </section>
  <p class="label" style="left:150px">option 1</p>

  <section class="piece fax" aria-label="Fax cover sheet">
    <span class="brand">Velin Medical</span>
    <div class="contact">
      12345 any street<br>city, state 98765<br>T (555) 201-7780<br>F (555) 201-7781<br>velinmedical.net
    </div>
    <h1>FAX</h1>
    <div class="form">
      <div class="field">To:</div><div class="field">From:</div>
      <div class="field">Fax:</div><div class="field">Pages:</div>
      <div class="field">Phone:</div><div class="field">Date:</div>
      <div class="field">Re:</div><div class="field">CC:</div>
    </div>
    <div class="checks">
      <span>Urgent</span><span>For Review</span><span>Please Comment</span><span>Please Reply</span><span>Please Recycle</span>
    </div>
    <span class="watermark" aria-hidden="true">Velin Medical</span>
    <div class="band" style="justify-content:center"><span>www.velinmedical.net</span></div>
  </section>
  <p class="label" style="left:528px">option 2</p>

  <section class="piece envelope env-back" aria-label="Envelope back">
    <svg width="190" height="155" viewBox="0 0 190 155"><polygon points="0,0 190,0 190,50 120,88 70,88 0,50" fill="var(--slate)"/></svg>
    <span class="brand on-dark">Velin Medical</span>
  </section>

  <section class="piece envelope env-grey" aria-label="Envelope back, grey flap">
    <svg width="305" height="148" viewBox="0 0 305 148"><polygon points="0,0 305,0 305,34 190,64 115,64 0,34" fill="var(--grey-flap)"/></svg>
    <span class="url">www.velinmedical.net</span>
  </section>

  <section class="piece env-front" aria-label="Envelope front">
    <div class="flap"></div>
    <span class="brand">Velin Medical</span>
    <p class="address">12345 any street<br>city, state 98765</p>
    <span class="url">www.velinmedical.net</span>
    <div class="stripe"></div>
  </section>

  <section class="piece card-front" aria-label="Business card front">
    <div class="top">T (555) 201-7780</div>
    <span class="brand">Velin Medical</span>
    <p class="lines">Tobias Morvel, CEO<br>12345 any street, city, state 98765<br>tmorvel@velinmedical.net</p>
  </section>

  <section class="piece card-back" aria-label="Business card back">
    <span class="brand on-dark">Velin Medical</span>
  </section>

</body>
</html>
```